Hot young IT advisor needs business cards as upscale and innovative as they are

We need business cards that make a statement about who we are, as a young and upscale IT advisor. Our whole angle is innovation and tenacity in our personal relationships with our clients. We've just done a brand overhaul and need cards that have the new logos, but we're also looking for someone with a sixth sense who can capture what sets us apart and communicate that with a business card. Clean, minimalist, upscale, innovative, personal. Our budget only allows room for them to be soft-touch, no spot gloss or foil designs please.

Target Market(s)

High-level decision makers at middle-market and large organizations in the healthcare, financial services, sports and entertainment, K-12 education, college and university, state and local government, and federal government sectors.

Industry/Entity Type

Information Technology

Font styles to use
Sans Serif

Colors
ec1f27
606060
ffffff

Requirements
Should not have
• Designs with low contrast which would require spot-gloss or embossing.

```html
<!DOCTYPE html>
<html lang="en">
<head>
<meta charset="utf-8">
<title>Norvane Advisory Business Card</title>
<link href="https://fonts.googleapis.com/css2?family=Rubik:wght@400;500&display=swap" rel="stylesheet">
<style>
  :root {
    --brand-red: #ec1f27;
    --brand-grey: #606060;
    --brand-white: #ffffff;
    --paper: #efefed;
    --card-dark: #221e1f;
    --stage: #1c1c1c;
    --ink: #2a2a2a;
  }
  * { box-sizing: border-box; margin: 0; padding: 0; }
  html, body {
    width: 1200px; height: 1200px; overflow: hidden;
    background: var(--stage);
    font-family: "Rubik", sans-serif;
  }
  .canvas { position: relative; width: 1200px; height: 1200px; }
  .card {
    position: absolute; left: 200px; width: 800px; height: 457px;
    border-radius: 26px; overflow: hidden;
  }
  .card-front {
    top: 110px; background: var(--paper);
    display: flex; align-items: center; justify-content: center;
  }
  .company-name {
    font-weight: 500; letter-spacing: 0.01em; white-space: nowrap;
  }
  .card-front .company-name { color: var(--ink); font-size: 34px; }
  .card-back {
    top: 630px;
    background: linear-gradient(160deg, #2a2526 0%, var(--card-dark) 60%, #1b1819 100%);
  }
  .brand-feature {
    position: absolute; left: 70px; top: 0; width: 330px; height: 330px;
    background: linear-gradient(180deg, rgba(236,31,39,0.85) 0%, rgba(236,31,39,0.35) 70%, rgba(236,31,39,0) 100%);
    border-radius: 0 0 18px 18px;
  }
  .card-back .company-name {
    position: absolute; left: 56px; bottom: 58px;
    color: var(--brand-white); font-size: 32px;
  }
  .contact {
    position: absolute; left: 470px; top: 118px; color: var(--brand-white);
  }
  .contact-name { font-size: 27px; font-weight: 500; letter-spacing: 0.02em; }
  .contact-title { font-size: 17px; color: var(--brand-red); letter-spacing: 0.04em; margin-top: 2px; }
  .contact-list { list-style: none; margin-top: 22px; }
  .contact-list li {
    display: flex; align-items: center; gap: 14px;
    font-size: 18px; letter-spacing: 0.05em; margin-bottom: 10px;
  }
  .icon-badge {
    width: 24px; height: 24px; border-radius: 50%;
    background: var(--brand-red);
    display: flex; align-items: center; justify-content: center;
  }
  .address {
    margin-top: 22px; font-size: 18px; line-height: 1.45; letter-spacing: 0.05em;
    font-style: normal;
  }
</style>
</head>
<body>
<main class="canvas">
  <section class="card card-front">
    <div class="company-name">Norvane Advisory</div>
  </section>

  <section class="card card-back">
    <div class="brand-feature" role="img" aria-label="Large red brand decoration with a dotted data-stream pattern"></div>
    <div class="company-name">Norvane Advisory</div>

    <div class="contact">
      <div class="contact-name">Daniel Whitaker</div>
      <div class="contact-title">Managing Director</div>
      <ul class="contact-list">
        <li>
          <span class="icon-badge">
            <svg width="13" height="13" viewBox="0 0 24 24"><path fill="#fff" d="M6.6 10.8a15.1 15.1 0 0 0 6.6 6.6l2.2-2.2c.3-.3.7-.4 1-.2 1.1.4 2.3.6 3.6.6.6 0 1 .4 1 1V20c0 .6-.4 1-1 1A17 17 0 0 1 3 4c0-.6.4-1 1-1h3.5c.6 0 1 .4 1 1 0 1.3.2 2.5.6 3.6.1.3 0 .7-.2 1z"/></svg>
          </span>
          555-013-2048
        </li>
        <li>
          <span class="icon-badge">
            <svg width="13" height="13" viewBox="0 0 24 24"><rect x="3" y="5" width="18" height="14" rx="1.5" fill="#fff"/><path d="M3.5 6l8.5 7 8.5-7" fill="none" stroke="#ec1f27" stroke-width="1.8"/></svg>
          </span>
          hello@norvane.com
        </li>
        <li>
          <span class="icon-badge">
            <svg width="14" height="14" viewBox="0 0 24 24" fill="none" stroke="#fff" stroke-width="1.8"><circle cx="12" cy="12" r="9"/><ellipse cx="12" cy="12" rx="4" ry="9"/><path d="M3 12h18M5 7h14M5 17h14"/></svg>
          </span>
          www.norvane.com
        </li>
      </ul>
      <address class="address">
        180 Linden Street NE<br>
        Suite 300, Fairhaven<br>
        OR 97100
      </address>
    </div>
  </section>
</main>
</body>
</html>
```